Commercial construction business needs a great sales brochure!

We are smaller commercial construction company in the Minneapolis, MN market that is looking for a professional sales brochure that can be used to market our services at trade shows or meetings with potential clients. We provide commercial membrane flat roofing, siding and construction services. The final design should communicate trust, growth and safety.

```html
<!DOCTYPE html>
<html lang="en">
<head>
<meta charset="utf-8">
<title>Ridgeline Commercial – Roofing Services Experts</title>
<link rel="stylesheet" href="https://fonts.googleapis.com/css2?family=Lato:wght@300;400;700&family=Raleway:wght@300;800&display=swap">
<style>
  :root {
    --red: #a3111a;
    --red-deep: #7e0b12;
    --charcoal: #4a4a4c;
    --ink: #2c2c2e;
    --white: #ffffff;
    --paper: #f4f4f4;
    --badge: #b9b9bb;
  }
  * { margin: 0; padding: 0; box-sizing: border-box; }
  html, body { width: 848px; height: 1200px; overflow: hidden; background: var(--white); }
  .brochure { position: relative; width: 848px; height: 1200px; overflow: hidden; font-family: "Lato", sans-serif; color: var(--ink); }
  .art { position: absolute; inset: 0; }

  .brand { position: absolute; top: 36px; left: 385px; width: 340px; text-align: center; }
  .brand-mark { display: inline-block; width: 54px; height: 54px; background: var(--red); margin-bottom: 10px; }
  .brand-name { font-family: "Raleway", sans-serif; font-weight: 800; font-size: 15px; color: var(--red); letter-spacing: .3px; line-height: 1.2; }
  .brand-sub { font-size: 7px; letter-spacing: 1.6px; color: var(--red); }
  .website { position: absolute; top: 138px; left: 352px; width: 406px; text-align: center; font-size: 22px; letter-spacing: .6px; color: var(--ink); }

  .headline { position: absolute; top: 292px; left: 52px; color: var(--white); font-family: "Raleway", sans-serif; }
  .headline .strong { display: block; font-weight: 800; font-size: 46px; line-height: 44px; letter-spacing: .5px; }
  .headline .light { display: block; font-weight: 300; font-size: 42px; line-height: 50px; letter-spacing: 1px; }

  .services { position: absolute; top: 486px; left: 56px; list-style: none; color: var(--white); }
  .services li { display: flex; align-items: center; font-size: 28px; line-height: 37px; letter-spacing: .3px; }
  .services svg { width: 20px; height: 20px; margin-right: 11px; flex: none; }

  .accreditations { position: absolute; top: 1031px; left: 0; width: 372px; text-align: center; font-size: 15px; letter-spacing: 3px; color: var(--ink); }
  .badge { position: absolute; background: var(--badge); border-radius: 2px; }

  .contact { position: absolute; top: 1028px; left: 492px; color: var(--white); }
  .phone-row { display: flex; align-items: center; }
  .phone-icon { width: 44px; height: 44px; margin-right: 14px; }
  .emergency { font-size: 17px; letter-spacing: .4px; }
  .phone { font-size: 25px; font-weight: 700; letter-spacing: .4px; line-height: 1.05; }
  .rule { width: 257px; height: 4px; background: var(--red); margin: 8px 0 10px 58px; }
  .details { margin-left: 58px; font-size: 14.5px; line-height: 19px; letter-spacing: .8px; }
</style>
</head>
<body>
<div class="brochure">
  <svg class="art" width="848" height="1200" viewBox="0 0 848 1200">
    <defs>
      <linearGradient id="houseTone" x1="0" y1="0" x2="1" y2="1">
        <stop offset="0" stop-color="#2f4a26"/>
        <stop offset=".45" stop-color="#8d7f79"/>
        <stop offset=".75" stop-color="#c9bfba"/>
        <stop offset="1" stop-color="#6d6a66"/>
      </linearGradient>
      <linearGradient id="storeTone" x1="0" y1="0" x2="0" y2="1">
        <stop offset="0" stop-color="#5b93d6"/>
        <stop offset=".45" stop-color="#a6805c"/>
        <stop offset="1" stop-color="#c8bfb2"/>
      </linearGradient>
      <linearGradient id="metalTone" x1="0" y1="0" x2="1" y2="1">
        <stop offset="0" stop-color="#4a4237"/>
        <stop offset=".5" stop-color="#b9bec2"/>
        <stop offset="1" stop-color="#6f6f6a"/>
      </linearGradient>
      <linearGradient id="windowTone" x1="0" y1="0" x2="1" y2="0">
        <stop offset="0" stop-color="#8a5a3c"/>
        <stop offset=".5" stop-color="#d9d3c8"/>
        <stop offset="1" stop-color="#7a4b33"/>
      </linearGradient>
    </defs>

    <rect x="248" y="187" width="600" height="582" fill="url(#houseTone)" role="img" aria-label="Aerial photo of a two-storey home with a new grey shingle roof among trees"/>
    <polygon points="0,0 139,0 582,769 0,769" fill="var(--red)" opacity=".93"/>
    <polygon points="0,0 139,0 380,420 0,700" fill="var(--red-deep)" opacity=".35"/>

    <polygon points="0,769 394,769 364,991 0,991" fill="url(#storeTone)" role="img" aria-label="Photo of a finished commercial storefront with brick and wood-tone siding"/>
    <polygon points="370,769 620,769 620,991 340,991" fill="url(#metalTone)" role="img" aria-label="Photo of a standing-seam metal roof"/>
    <rect x="620" y="769" width="228" height="222" fill="url(#windowTone)" role="img" aria-label="Photo of new white double-hung windows in a brick facade"/>

    <polygon points="385,991 848,991 848,1200 502,1200" fill="var(--charcoal)"/>
  </svg>

  <div class="brand">
    <span class="brand-mark"></span>
    <div class="brand-name">RIDGELINE COMMERCIAL</div>
    <div class="brand-sub">ROOFING &amp; CONSTRUCTION</div>
  </div>
  <div class="website">www.ridgelinecommercial.com</div>

  <h1 class="headline">
    <span class="strong">ROOFING</span>
    <span class="strong">SERVICES</span>
    <span class="light">EXPERTS</span>
  </h1>

  <ul class="services">
    <li><svg viewBox="0 0 20 20"><circle cx="10" cy="10" r="10" fill="#fff"/><path d="M5.5 10.2l3 3 6-6.2" fill="none" stroke="#a3111a" stroke-width="2.4" stroke-linecap="round" stroke-linejoin="round"/></svg>Roofing</li>
    <li><svg viewBox="0 0 20 20"><circle cx="10" cy="10" r="10" fill="#fff"/><path d="M5.5 10.2l3 3 6-6.2" fill="none" stroke="#a3111a" stroke-width="2.4" stroke-linecap="round" stroke-linejoin="round"/></svg>Siding</li>
    <li><svg viewBox="0 0 20 20"><circle cx="10" cy="10" r="10" fill="#fff"/><path d="M5.5 10.2l3 3 6-6.2" fill="none" stroke="#a3111a" stroke-width="2.4" stroke-linecap="round" stroke-linejoin="round"/></svg>Window Installation</li>
    <li><svg viewBox="0 0 20 20"><circle cx="10" cy="10" r="10" fill="#fff"/><path d="M5.5 10.2l3 3 6-6.2" fill="none" stroke="#a3111a" stroke-width="2.4" stroke-linecap="round" stroke-linejoin="round"/></svg>Construction Services</li>
    <li><svg viewBox="0 0 20 20"><circle cx="10" cy="10" r="10" fill="#fff"/><path d="M5.5 10.2l3 3 6-6.2" fill="none" stroke="#a3111a" stroke-width="2.4" stroke-linecap="round" stroke-linejoin="round"/></svg>Repair Services</li>
    <li><svg viewBox="0 0 20 20"><circle cx="10" cy="10" r="10" fill="#fff"/><path d="M5.5 10.2l3 3 6-6.2" fill="none" stroke="#a3111a" stroke-width="2.4" stroke-linecap="round" stroke-linejoin="round"/></svg>Insurance Restoration</li>
  </ul>

  <div class="accreditations">ACREDITATIONS</div>
  <span class="badge" style="left:80px;top:1063px;width:76px;height:28px"></span>
  <span class="badge" style="left:214px;top:1063px;width:124px;height:26px"></span>
  <span class="badge" style="left:42px;top:1126px;width:68px;height:32px"></span>
  <span class="badge" style="left:141px;top:1120px;width:42px;height:40px"></span>
  <span class="badge" style="left:207px;top:1120px;width:50px;height:44px"></span>
  <span class="badge" style="left:275px;top:1132px;width:96px;height:20px"></span>

  <div class="contact">
    <div class="phone-row">
      <svg class="phone-icon" viewBox="0 0 44 44">
        <circle cx="22" cy="22" r="19.5" fill="none" stroke="#fff" stroke-width="3"/>
        <path d="M15.5 12.5l4 .3 2 5-2.6 2a13 13 0 0 0 6.3 6.3l2-2.6 5 2 .3 4c-.2 1.6-1.7 2.6-3.3 2.5C19.8 31.2 12.8 24.2 12 15.8c-.1-1.6 1-3.1 2.5-3.3z" fill="#fff"/>
      </svg>
      <div>
        <div class="emergency">24-HOUR EMERGENCY SERVICE</div>
        <div class="phone">(612) 555-0148</div>
      </div>
    </div>
    <div class="rule"></div>
    <div class="details">
      info@ridgelinecommercial.com<br>
      2450 Birchwood Ln<br>
      Cedar Bay, MN 55390<br>
      Mon – Fri. 7.00 – 5.00
    </div>
  </div>
</div>
</body>
</html>
```